User-interface and web design for new forum-style communication platform

We developed a new forum-style communication platform specially targetting stock investors to share and discuss information on companies listed on the stock exchange.

You have complete freedom for designing the user-interface and web design. Designs should include all features listed below.

Please read the attached document for full specifications. Also attached is a mockup of the layout, but this is only directional. A mockup for the user-profile is also attached, but does not need to be designed.

This project focusses on the homepage and thread view.

The winner(s) will be asked to design the complete project. (create thread box, user profile, registering, settings...)

We are looking for a well thought out, smart design that incorporates the specifications in the attached document. Please do not hesitate to contact us if anything is not clear.

Target Market(s)

Stock investors from 25 to 60 years old (the people that are currently on investor forums)

Industry/Entity Type

Communication

Font styles to use
Sans Serif

Colors

Designer to choose colors to be used in the design.

Requirements
Must have
• Full homepage design & Thread view specified in the attached document.
Nice to have
• Create thread view
- Field for adding tags
- field for subject of the thread
- text box with basic text editing
- method for sharing media
Should not have
• Logo design.

```html
<!DOCTYPE html>
<html lang="en">
<head>
<meta charset="utf-8">
<title>Forum – Thread View</title>
<link rel="stylesheet" href="https://fonts.googleapis.com/css2?family=Lato:wght@400;700&display=swap">
<style>
:root{
  --orange:#e8502a;
  --orange-dark:#c9401f;
  --page:#efefef;
  --panel:#ffffff;
  --ink:#2b2b2b;
  --text:#8a8a8a;
  --muted:#b5b5b5;
  --line:#dddddd;
  --rule:#e6e6e6;
  --btn-icon:#c9c9c9;
  --btn-label:#dcdcdc;
  --placeholder:#f4f4f4;
}
*{box-sizing:border-box;margin:0;padding:0}
html,body{width:1200px;height:1200px;overflow:hidden}
body{background:var(--page);font-family:"Lato",Arial,sans-serif;color:var(--ink)}
.stage{position:relative;width:1000px;height:1000px;transform:scale(1.2);transform-origin:0 0}
.abs{position:absolute}

/* sidebar */
.logo-box{left:113px;top:41px;width:258px;height:112px;background:var(--panel);display:flex;align-items:center;justify-content:center;font-size:19px;font-weight:700;color:var(--ink)}
.profile-box{left:113px;top:162px;width:258px;height:111px;background:var(--panel)}
.profile-name{position:absolute;left:7px;top:10px;font-size:15px}
.search{position:absolute;left:7px;top:47px;width:243px;height:33px;border:1px solid var(--line);display:flex}
.search span{flex:1;font-size:11px;color:var(--muted);padding:9px 7px}
.search b{width:40px;background:var(--orange);display:flex;align-items:center;justify-content:center;margin:-1px -1px -1px 0}
.side-panel{left:113px;width:258px;background:var(--panel);border-bottom:2px solid var(--orange)}
.side-head{height:32px;background:var(--orange);color:#fff;font-size:13px;font-weight:700;padding:9px 7px}
.side-item{margin:0 10px 0 7px;border-bottom:1px dotted #9a9a9a;padding:13px 0 10px}
.side-item h4{font-size:11px;font-weight:400;color:var(--ink);margin-bottom:5px}
.side-item p{font-size:9px;color:var(--text);line-height:13px}
.side-item a{color:var(--orange);text-decoration:none}
.show-all{display:block;width:97px;margin:13px auto 0;height:14px;background:var(--orange);color:#fff;font-size:10px;text-align:center;line-height:14px}

/* main */
.main{left:371px;top:41px;width:516px;height:911px;background:var(--panel);box-shadow:0 0 6px rgba(0,0,0,.12)}
.follower{left:662px;top:24px;width:48px;height:25px;background:#fff;border:1px solid var(--line);border-radius:3px;font-size:8px;color:var(--orange);text-align:center;line-height:10px;padding-top:3px}
.user-select{left:725px;top:49px;width:155px;height:23px;border:1px solid var(--line);display:flex;font-size:10px;font-weight:700;color:var(--orange)}
.user-select span{flex:1;padding:5px 8px}
.user-select b{width:25px;border-left:1px solid var(--line);display:flex;align-items:center;justify-content:center}
.topic-bar{left:378px;top:89px;width:501px;height:56px;background:var(--orange);padding:8px 9px}
.topic-field{background:#fff;height:39px;display:flex;align-items:center;padding:4px}
.topic-field span{flex:1;font-size:10px;color:var(--muted);padding-left:5px}
.topic-field i{font-style:normal;width:48px;height:31px;color:#fff;font-size:9px;font-weight:700;display:flex;align-items:center;justify-content:center}
.btn-save{background:var(--orange-dark)}.btn-clear{background:var(--orange)}
.rule{left:379px;width:500px;height:4px;background:var(--rule)}
.crumbs{left:379px;top:175px;font-size:11px;color:var(--ink);display:flex;gap:4px;align-items:center}
.tab{top:234px;width:88px;height:23px;background:var(--orange);color:#fff;font-size:11px;font-weight:700;text-align:center;line-height:23px}
.create{left:774px;top:291px;width:105px;height:23px;background:var(--orange);color:#fff;font-size:9px;font-weight:700;text-align:center;line-height:23px}

/* thread */
.thread{left:379px;width:560px;height:218px}
.thread-tab{position:absolute;left:8px;top:0;width:104px;height:22px;background:var(--orange);color:#fff;font-size:10px;font-weight:700;text-align:center;line-height:22px}
.thread-card{position:absolute;left:0;top:22px;width:500px;height:195px;border:1px solid var(--line)}
.thread-image{position:absolute;left:7px;top:8px;width:162px;height:137px;background:var(--placeholder);border:1px solid var(--line);display:flex;align-items:center;justify-content:center;font-size:13px;color:var(--ink)}
.date{position:absolute;left:185px;top:8px;width:31px;border:1px solid var(--orange)}
.date b{display:block;background:var(--orange);color:#fff;font-size:11px;font-weight:400;text-align:center;height:16px;line-height:16px}
.date span{display:block;font-size:8px;text-align:center;height:12px;line-height:12px;color:var(--ink)}
.thread-title{position:absolute;left:224px;top:4px;font-size:19px;font-weight:400}
.thread-meta{position:absolute;left:224px;top:27px;font-size:14px;color:var(--ink)}
.thread-meta em{font-style:normal;color:var(--muted)}
.thread-dots{position:absolute;left:185px;top:56px;width:306px;border-top:1px dotted #8a8a8a}
.thread-body{position:absolute;left:185px;top:70px;width:312px;font-size:10.6px;line-height:17.6px;color:var(--text)}
.thread-foot{position:absolute;left:0;right:0;top:153px;border-top:1px solid var(--line)}
.btns{position:absolute;top:161px;height:23px;display:flex;gap:1px}
.btns .ic{width:24px;height:23px;background:var(--btn-icon);display:flex;align-items:center;justify-content:center}
.btns .lb{height:23px;background:var(--btn-label);color:#fff;font-size:9px;line-height:23px;padding:0 12px}
.side-acts{position:absolute;left:501px;width:55px}
.act{position:absolute;left:0;height:22px;display:flex;font-size:8px;color:#fff}
.act .ic{width:22px;background:var(--btn-icon);display:flex;align-items:center;justify-content:center;font-size:13px}
.act .lb{background:var(--btn-label);padding:0 6px;line-height:22px;width:33px}
.reply-box{left:402px;top:556px;width:477px;height:65px;border:1px solid var(--line)}
.reply-avatar{position:absolute;left:8px;top:7px;width:50px;height:50px;background:var(--placeholder);border:1px solid var(--line)}
.reply-box span{position:absolute;left:73px;top:6px;font-size:10px;color:var(--text)}
.divider{left:379px;top:637px;width:500px;border-top:1px dashed var(--line)}
</style>
</head>
<body>
<div class="stage">

  <!-- sidebar -->
  <div class="abs logo-box">Your Company Logo</div>
  <div class="abs profile-box">
    <div class="profile-name">Jerome Doe</div>
    <div class="search"><span>Search...</span><b><svg width="14" height="14" viewBox="0 0 14 14"><circle cx="8.5" cy="5.5" r="4" fill="none" stroke="#fff" stroke-width="1.6"/><line x1="5.6" y1="8.4" x2="1.5" y2="12.5" stroke="#fff" stroke-width="1.8"/></svg></b></div>
  </div>

  <div class="abs side-panel" style="top:282px">
    <div class="side-head">Saved Filter</div>
    <div class="side-item"><h4>Lorem Ipsum</h4><p>Voluptatem nam ligula sit est est lectus.</p></div>
    <div class="side-item"><h4>Duis Dapibus</h4><p>Interdum suspendisse id dolor sem erat est.</p></div>
    <div class="side-item" style="border:0"><h4>Duis Ullamcorper</h4><p>Vestibulum aliquam arcu aenean, placerat vestibulum</p></div>
    <span class="show-all" style="margin-top:6px">Show all +</span>
  </div>

  <div class="abs side-panel" style="top:508px">
    <div class="side-head">Popular Tags</div>
    <div class="side-item" style="padding-top:14px"><h4>Duis Ullamcorper</h4><p>Duis Ullamcorper,metus a dapibus euismod,velit enim varius mi tristique diam . <a>Read More &gt;&gt;</a></p></div>
    <div class="side-item"><h4>Lorem Ipsum</h4><p>Duis Ullamcorper,metus a dapibus euismod,velit enim varius mi tristique diam . <a>Read More &gt;&gt;</a></p></div>
    <span class="show-all" style="margin-top:25px">Show all +</span>
  </div>

  <div class="abs side-panel" style="top:734px">
    <div class="side-head">Popular Contribution</div>
    <div class="side-item" style="padding-top:14px"><h4>Duis Ullamcorper</h4><p>Duis Ullamcorper,metus a dapibus euismod,velit enim varius mi tristique diam . <a>Read More &gt;&gt;</a></p></div>
    <div class="side-item"><h4>Lorem Ipsum</h4><p>Duis Ullamcorper,metus a dapibus euismod,velit enim varius mi tristique diam . <a>Read More &gt;&gt;</a></p></div>
    <span class="show-all" style="margin-top:25px">Show all +</span>
  </div>

  <!-- main -->
  <div class="abs main"></div>
  <div class="abs follower">4<br>Follower</div>
  <svg class="abs" style="left:684px;top:49px" width="28" height="22" viewBox="0 0 28 22"><circle cx="17" cy="5" r="4.5" fill="#e8502a"/><path d="M9 21c0-6 3.5-9 8-9s8 3 8 9z" fill="#e8502a"/><circle cx="8" cy="7" r="4" fill="#e8502a"/><path d="M1 21c0-5.5 3-8 7-8 2 0 3 .5 4 1.2-2 1.6-3 4-3 6.8z" fill="#e8502a"/></svg>
  <div class="abs user-select"><span>Jerome Doe</span><b><svg width="10" height="7" viewBox="0 0 10 7"><path d="M1 1l4 4 4-4" fill="none" stroke="#e8502a" stroke-width="2"/></svg></b></div>

  <div class="abs topic-bar"><div class="topic-field"><span># Lorem Ipsum</span><i class="btn-save">Save</i><i class="btn-clear">Clear</i></div></div>
  <div class="abs rule" style="top:154px"></div>

  <div class="abs crumbs">Home
    <svg width="6" height="9" viewBox="0 0 6 9"><path d="M1 1l3.5 3.5L1 8" fill="none" stroke="#e8502a" stroke-width="2"/></svg>Conservation
    <svg width="6" height="9" viewBox="0 0 6 9"><path d="M1 1l3.5 3.5L1 8" fill="none" stroke="#e8502a" stroke-width="2"/></svg>Public
    <svg width="6" height="9" viewBox="0 0 6 9"><path d="M1 1l3.5 3.5L1 8" fill="none" stroke="#e8502a" stroke-width="2"/></svg>Lorem Ipsum
  </div>

  <div class="abs tab" style="left:379px">Public</div>
  <div class="abs tab" style="left:476px">Following</div>
  <div class="abs tab" style="left:573px">Contact</div>
  <div class="abs rule" style="top:273px"></div>
  <div class="abs create">Create Thread</div>

  <!-- thread 1 -->
  <div class="abs thread" style="top:324px">
    <div class="thread-tab">Thread 1</div>
    <div class="thread-card">
      <div class="thread-image" role="img" aria-label="Thread image placeholder">Image</div>
      <div class="date"><b>24</b><span>JAN</span></div>
      <div class="thread-title">Lorem Ipsum</div>
      <div class="thread-meta">Posted by : <em>Jerome Doe . On 21 : 24</em></div>
      <div class="thread-dots"></div>
      <p class="thread-body">Lorem ipsum dolor is amet,consecttetur adipiscing elit. integer dictum, magna id aliquam aliquet,nulla turpis tempus metus,vit sulicitudin nisl nitic ut neque.ut at felis a neque sollicitudin eges tas.Lorem ipsum dolor is amet,consecttetur adipiscing elit.</p>
      <div class="thread-foot"></div>
      <div class="btns" style="left:225px"><span class="ic"><svg width="12" height="11" viewBox="0 0 12 11"><path d="M1 1h10v7H5l-3 2V8H1z" fill="none" stroke="#fff" stroke-width="1.2"/></svg></span><span class="lb">Reply</span></div>
      <div class="btns" style="left:306px"><span class="ic"><svg width="11" height="11" viewBox="0 0 11 11"><path d="M2 10V6c0-2 1.5-3 3.5-3H9M7 1l2.5 2L7 5" fill="none" stroke="#fff" stroke-width="1.5"/></svg></span><span class="ic"><svg width="6" height="6"><circle cx="3" cy="3" r="3" fill="#fff"/></svg></span><span class="ic"><svg width="6" height="6"><circle cx="3" cy="3" r="3" fill="#fff"/></svg></span><span class="ic"><svg width="6" height="6"><circle cx="3" cy="3" r="3" fill="#fff"/></svg></span></div>
      <div class="btns" style="left:411px"><span class="ic"><svg width="12" height="12" viewBox="0 0 12 12"><path d="M6 .5l1.7 3.6 3.8.4-2.9 2.6.9 3.9L6 9l-3.5 2 .9-3.9L.5 4.5l3.8-.4z" fill="#fff"/></svg></span><span class="lb">Favourite</span></div>
    </div>
    <div class="side-acts">
      <div class="act" style="top:32px"><span class="ic">+</span><span class="lb">More</span></div>
      <div class="act" style="top:63px"><span class="lb" style="width:55px;background:var(--btn-label)">12 reply</span></div>
      <div class="act" style="top:96px"><span class="ic"><svg width="10" height="10" viewBox="0 0 10 10"><circle cx="5" cy="3" r="2.5" fill="#fff"/><path d="M0 10c0-3 2-4.5 5-4.5s5 1.5 5 4.5z" fill="#fff"/></svg></span><span class="lb">250</span></div>
    </div>
  </div>

  <div class="abs reply-box"><div class="reply-avatar"></div><span>type you reply here......</span></div>
  <div class="abs divider"></div>

  <!-- thread 2 -->
  <div class="abs thread" style="top:654px">
    <div class="thread-tab">Thread 2</div>
    <div class="thread-card">
      <div class="thread-image" role="img" aria-label="Thread image placeholder">Image</div>
      <div class="date"><b>26</b><span>JAN</span></div>
      <div class="thread-title">Duis Dapibus</div>
      <div class="thread-meta">Posted by : <em>Jerome Doe . On 11 : 24</em></div>
      <div class="thread-dots"></div>
      <p class="thread-body">Lorem ipsum dolor is amet,consecttetur adipiscing elit. integer dictum, magna id aliquam aliquet,nulla turpis tempus metus,vit sulicitudin nisl nitic ut neque.ut at felis a neque sollicitudin eges tas.Lorem ipsum dolor is amet,consecttetur adipiscing elit.</p>
      <div class="thread-foot"></div>
      <div class="btns" style="left:225px"><span class="ic"><svg width="12" height="11" viewBox="0 0 12 11"><path d="M1 1h10v7H5l-3 2V8H1z" fill="none" stroke="#fff" stroke-width="1.2"/></svg></span><span class="lb">Reply</span></div>
      <div class="btns" style="left:306px"><span class="ic"><svg width="11" height="11" viewBox="0 0 11 11"><path d="M2 10V6c0-2 1.5-3 3.5-3H9M7 1l2.5 2L7 5" fill="none" stroke="#fff" stroke-width="1.5"/></svg></span><span class="ic"><svg width="6" height="6"><circle cx="3" cy="3" r="3" fill="#fff"/></svg></span><span class="ic"><svg width="6" height="6"><circle cx="3" cy="3" r="3" fill="#fff"/></svg></span><span class="ic"><svg width="6" height="6"><circle cx="3" cy="3" r="3" fill="#fff"/></svg></span></div>
      <div class="btns" style="left:411px"><span class="ic"><svg width="12" height="12" viewBox="0 0 12 12"><path d="M6 .5l1.7 3.6 3.8.4-2.9 2.6.9 3.9L6 9l-3.5 2 .9-3.9L.5 4.5l3.8-.4z" fill="#fff"/></svg></span><span class="lb">Favourite</span></div>
    </div>
    <div class="side-acts">
      <div class="act" style="top:33px"><span class="ic">+</span><span class="lb">More</span></div>
      <div class="act" style="top:64px"><span class="lb" style="width:55px">12 reply</span></div>
      <div class="act" style="top:97px"><span class="ic"><svg width="10" height="10" viewBox="0 0 10 10"><circle cx="5" cy="3" r="2.5" fill="#fff"/><path d="M0 10c0-3 2-4.5 5-4.5s5 1.5 5 4.5z" fill="#fff"/></svg></span><span class="lb">250</span></div>
    </div>
  </div>

</div>
</body>
</html>
```